Qorvane VoIP COMMERCIAL PHONE FLYER

We are a full service telecom VoIP company that offers local, long distance calling plans to business clients. We offer local installations, and local service we have a hands on approach and will match or beat any competitor. We work with all types of business. We are fully HIPPA complient in the medical field

Target Market(s)

SMALL TO MEDIUM BUSINESS, Medical, Real Estate, Lawyer, Accounting

Industry/Entity Type

VoIP

Font styles to use
Serif

Colors
0054AA
0677BA
7BADD7
CADEEF
E8F1F8

Requirements
Must have
• Modern/ Current picture of phone reader friendly
Nice to have
• free flow, friendly, modern
Should not have
• stuffy, corporate feel

```html
<!DOCTYPE html>
<html lang="en">
<head>
<meta charset="utf-8">
<title>Qorvane VoIP Flyer</title>
<link rel="stylesheet" href="https://fonts.googleapis.com/css2?family=Barlow+Condensed:ital,wght@0,500;0,600;0,700;1,500&family=Open+Sans:wght@600&family=Quicksand:wght@600&display=swap">
<style>
  :root {
    --stage: #e8f1f8;
    --navy: #1b1a7c;
    --navy-deep: #15145f;
    --blue: #1f72b8;
    --blue-band: #2384c6;
    --blue-soft: #2a5fb0;
    --ink-title: #1a1a7a;
    --white: #ffffff;
    --photo-a: #3a4a66;
    --photo-b: #8fb4d8;
  }
  * { margin: 0; padding: 0; box-sizing: border-box; }
  html, body { width: 1200px; height: 800px; overflow: hidden; background: var(--stage); }
  .canvas { position: relative; width: 1200px; height: 800px; }
  .flyer {
    position: absolute; left: 300px; top: 11px;
    width: 694px; height: 900px;
    transform: scale(0.8645); transform-origin: top left;
    overflow: hidden; color: var(--white);
    font-family: "Barlow Condensed", sans-serif;
  }
  .flyer-bg { position: absolute; inset: 0; }
  .abs { position: absolute; }

  .brand { left: 32px; top: 40px; display: flex; align-items: center; gap: 14px; }
  .brand-dot { width: 34px; height: 34px; border-radius: 50%; background: var(--white); }
  .brand-name { font-size: 62px; font-weight: 700; line-height: 1; letter-spacing: 1px; }

  .tagline { left: 347px; top: 22px; line-height: 1; }
  .tagline-top { font-size: 33px; font-style: italic; font-weight: 500; color: var(--ink-title); }
  .tagline-main { font-size: 57px; font-style: italic; font-weight: 500; margin-top: 4px; }

  .phone-photo {
    left: 24px; top: 112px; width: 340px; height: 282px; border-radius: 14px;
    background: linear-gradient(135deg, var(--photo-a), var(--photo-b));
  }

  .perks { left: 374px; top: 192px; list-style: none; font-family: "Open Sans", sans-serif; font-size: 14.5px; line-height: 24px; }
  .perks li { display: flex; gap: 10px; margin-bottom: 7px; }
  .perks svg { flex: none; margin-top: 2px; }

  .help { left: 62px; top: 398px; font-size: 41px; font-weight: 500; }
  .save-band { left: 0; top: 453px; width: 694px; height: 107px; background: var(--blue-band); }
  .save { left: 56px; top: 447px; font-size: 100px; font-weight: 700; line-height: 1.1; letter-spacing: 1px; }
  .percent {
    left: 492px; top: 428px; width: 148px; height: 148px; border-radius: 50%;
    background: var(--navy); border: 3px solid var(--white);
    display: flex; align-items: center; justify-content: center;
    font-size: 58px; font-weight: 600;
  }
  .bills { left: 60px; top: 566px; font-size: 38px; font-weight: 500; }

  .features { left: 60px; top: 632px; width: 600px; display: flex; }
  .feature { width: 190px; text-align: center; font-family: "Quicksand", sans-serif; font-size: 19px; line-height: 22px; letter-spacing: 0.5px; }
  .feature-icon { width: 92px; height: 92px; border-radius: 50%; background: var(--blue-band); margin: 0 auto 18px; display: flex; align-items: center; justify-content: center; }

  .contact-bar {
    left: 0; top: 813px; width: 694px; height: 87px; background: var(--blue);
    display: flex; align-items: center; justify-content: center; gap: 18px;
    font-family: "Quicksand", sans-serif; font-size: 15px;
  }
  .contact-item { display: flex; align-items: center; gap: 10px; }
  .contact-sep { width: 2px; height: 24px; background: var(--white); opacity: .8; }
</style>
</head>
<body>
<div class="canvas">
  <div class="flyer">
    <svg class="flyer-bg" width="694" height="900" viewBox="0 0 694 900" aria-hidden="true">
      <rect width="694" height="900" fill="var(--navy)"/>
      <circle cx="330" cy="330" r="230" fill="var(--blue-soft)" opacity=".55"/>
      <path d="M0 0H694V145H400C320 145 300 180 230 180C150 180 120 150 0 150Z" fill="var(--blue)"/>
      <path d="M0 150C120 150 150 180 230 180C300 180 320 145 400 145H694V200C560 200 520 230 420 230C300 230 260 195 0 210Z" fill="var(--blue-soft)" opacity=".6"/>
    </svg>

    <div class="abs brand"><span class="brand-dot"></span><span class="brand-name">Qorvane</span></div>

    <div class="abs tagline">
      <div class="tagline-top">YOUR BUSINESS</div>
      <div class="tagline-main">ON THE CLOUD</div>
    </div>

    <div class="abs phone-photo" role="img" aria-label="Photo of a modern desk video phone with handset and touch screen"></div>

    <ul class="abs perks">
      <li><svg width="22" height="22" viewBox="0 0 22 22"><circle cx="11" cy="11" r="9.5" fill="none" stroke="#fff" stroke-width="1.6"/><path d="M6 11l4 4 9-10" fill="none" stroke="#fff" stroke-width="1.8"/></svg>KEEP YOUR TELEPHONE NUMBERS</li>
      <li><svg width="22" height="22" viewBox="0 0 22 22"><circle cx="11" cy="11" r="9.5" fill="none" stroke="#fff" stroke-width="1.6"/><path d="M6 11l4 4 9-10" fill="none" stroke="#fff" stroke-width="1.8"/></svg><span>NO LONG TERM CONTRACTS<br>MONTH TO MONTH</span></li>
      <li><svg width="22" height="22" viewBox="0 0 22 22"><circle cx="11" cy="11" r="9.5" fill="none" stroke="#fff" stroke-width="1.6"/><path d="M6 11l4 4 9-10" fill="none" stroke="#fff" stroke-width="1.8"/></svg><span>THREE MONTHS FREE SERVICE<br>WITH ONE YEAR CONTRACT</span></li>
      <li><svg width="22" height="22" viewBox="0 0 22 22"><circle cx="11" cy="11" r="9.5" fill="none" stroke="#fff" stroke-width="1.6"/><path d="M6 11l4 4 9-10" fill="none" stroke="#fff" stroke-width="1.8"/></svg>HIPPA COMPLIANT</li>
      <li><svg width="22" height="22" viewBox="0 0 22 22"><circle cx="11" cy="11" r="9.5" fill="none" stroke="#fff" stroke-width="1.6"/><path d="M6 11l4 4 9-10" fill="none" stroke="#fff" stroke-width="1.8"/></svg>LOCAL SERVICE AND SUPPORT</li>
    </ul>

    <div class="abs help">WE HELP COMPANIES</div>
    <div class="abs save-band"></div>
    <div class="abs save">SAVE OVER</div>
    <div class="abs percent">30%</div>
    <div class="abs bills">ON THEIR MONTHLY PHONE BILLS</div>

    <div class="abs features">
      <div class="feature">
        <div class="feature-icon">
          <svg width="50" height="50" viewBox="0 0 50 50" fill="none" stroke="#fff" stroke-width="2.2" stroke-linecap="round"><path d="M17 26a10 10 0 1 1 16 0c-2 3-3 5-3 8H20c0-3-1-5-3-8z"/><path d="M20 38h10M21 42h8M25 4v4M10 10l3 3M40 10l-3 3M5 24h4M41 24h4"/></svg>
        </div>
        POWERFUL<br>FEATURES
      </div>
      <div class="feature">
        <div class="feature-icon">
          <svg width="52" height="50" viewBox="0 0 52 50" fill="none" stroke="#fff" stroke-width="2.2" stroke-linejoin="round"><path d="M6 20c0-8 7-13 15-13s15 5 15 13-7 13-15 13c-2 0-4 0-6-1l-7 4 2-6c-3-2-4-6-4-10z" fill="#fff" fill-opacity=".9"/><path d="M38 22c5 1 9 5 9 10 0 3-1 5-3 7l1 5-6-3c-7 2-15-1-17-7"/></svg>
        </div>
        EASY<br>TO USE
      </div>
      <div class="feature">
        <div class="feature-icon">
          <svg width="50" height="50" viewBox="0 0 50 50" fill="none" stroke="#fff" stroke-width="2.4" stroke-linecap="round" stroke-linejoin="round"><path d="M10 40L30 20M32 8a8 8 0 0 0 10 10l-4 4-6-6z"/><path d="M8 12l6-4 6 6-4 4zM18 18l22 22-3 3-22-22"/></svg>
        </div>
        EASY<br>SET UP
      </div>
    </div>

    <div class="abs contact-bar">
      <span class="contact-item"><svg width="22" height="22" viewBox="0 0 24 24" fill="none" stroke="#fff" stroke-width="1.8"><path d="M5 3l4 1 1 5-2 2c1 2 3 4 5 5l2-2 5 1 1 4-2 2C11 21 3 13 3 5z"/></svg>1555-010 2040</span>
      <span class="contact-sep"></span>
      <span class="contact-item"><svg width="24" height="20" viewBox="0 0 24 20" fill="none" stroke="#fff" stroke-width="1.8"><rect x="2" y="3" width="20" height="14" rx="1"/><path d="M2 4l10 8 10-8"/></svg>HELLO@QORVANE-VOICE.COM</span>
      <span class="contact-sep"></span>
      <span class="contact-item"><svg width="20" height="20" viewBox="0 0 24 24" fill="none" stroke="#fff" stroke-width="2" stroke-linecap="round"><path d="M10 14a5 5 0 0 0 7 0l4-4a5 5 0 0 0-7-7l-1 1M14 10a5 5 0 0 0-7 0l-4 4a5 5 0 0 0 7 7l1-1"/></svg>WWW.QORVANE-VOICE.COM</span>
    </div>
  </div>
</div>
</body>
</html>
```